Halcott Business Card Design

Photography business needs a logo. I would like to see creative licence on options on 1 & 2 sided. I really like the concept of a fully / partially frosted design. I have already used ArtisanHive for my Logo, so I am looking for the same level of assistance with this project.

Industry/Entity Type

Business

Font styles to use
Serif
Script

Requirements
Must have
• Must Have:
• - These are my contact details
• Name: Ames K Halcott
• Mobile: 5550193827
• email: lenorapaske@fernpost.net

```html
<!DOCTYPE html>
<html lang="en">
<head>
<meta charset="utf-8">
<title>Halcott Business Card Design</title>
<link href="https://fonts.googleapis.com/css2?family=Mr+Dafoe&family=Libre+Baskerville&family=Lato:wght@400&display=swap" rel="stylesheet">
<style>
  :root {
    --backdrop: #d9d9d9;
    --card-black: #0b0b0b;
    --card-charcoal: #2a2a2a;
    --silver-light: #f2f2f2;
    --silver-mid: #9a9a9a;
    --smoke-dark: #3c3c3c;
    --smoke-mid: #6a6a6a;
    --ink-white: #ffffff;
    --accent-cyan: #2fb4e6;
  }
  * { margin: 0; padding: 0; box-sizing: border-box; }
  html, body {
    width: 1200px;
    height: 918px;
    overflow: hidden;
    background: var(--backdrop);
  }
  .canvas {
    position: relative;
    width: 1200px;
    height: 918px;
  }
  .card {
    position: absolute;
    left: 300px;
    width: 600px;
    height: 343px;
    overflow: hidden;
    background: radial-gradient(ellipse at 30% 35%, var(--card-charcoal) 0%, var(--card-black) 70%);
    box-shadow: 0 10px 28px rgba(0,0,0,0.35);
  }
  .card--front { top: 86px; }
  .card--back { top: 489px; }
  .card__pattern {
    position: absolute;
    top: 0;
    left: 0;
    width: 600px;
    height: 343px;
  }
  .card__name {
    position: absolute;
    font-family: "Mr Dafoe", cursive;
    color: var(--ink-white);
    white-space: nowrap;
    line-height: 1;
    text-shadow: 0 3px 4px rgba(0,0,0,0.7);
  }
  .card--front .card__name {
    left: 44px;
    top: 108px;
    font-size: 66px;
  }
  .card--back .card__name {
    left: 190px;
    top: 200px;
    font-size: 60px;
  }
  .card__role {
    position: absolute;
    left: 400px;
    top: 264px;
    font-family: "Mr Dafoe", cursive;
    font-size: 28px;
    line-height: 1;
    color: var(--accent-cyan);
    white-space: nowrap;
  }
  .card__email--front {
    position: absolute;
    right: 28px;
    bottom: 24px;
    font-family: "Lato", sans-serif;
    font-size: 21px;
    color: var(--ink-white);
    white-space: nowrap;
  }
  .card__email--front .user { color: var(--accent-cyan); }
  .card__contact {
    position: absolute;
    left: 30px;
    top: 140px;
    font-family: "Libre Baskerville", serif;
    font-size: 11px;
    line-height: 20px;
    color: var(--ink-white);
    list-style: none;
    white-space: nowrap;
  }
  .card__contact .label { color: var(--accent-cyan); }
</style>
</head>
<body>
<main class="canvas">

  <section class="card card--front" aria-label="Business card front">
    <svg class="card__pattern" viewBox="0 0 600 343" role="img" aria-label="Frosted silver tribal stripe ornament sweeping across the right side">
      <defs>
        <linearGradient id="frostSilver" x1="0" y1="0" x2="1" y2="1">
          <stop offset="0" stop-color="#f2f2f2"/>
          <stop offset="0.55" stop-color="#9a9a9a"/>
          <stop offset="1" stop-color="#3c3c3c"/>
        </linearGradient>
      </defs>
      <path d="M250 0 C330 40 360 120 330 200 C310 260 350 320 420 343 L600 343 L600 20 C520 10 420 0 250 0 Z" fill="url(#frostSilver)" opacity="0.9"/>
    </svg>
    <div class="card__name">Ames K Halcott</div>
    <p class="card__email--front"><span class="user">lenorapaske</span>@fernpost.net</p>
  </section>

  <section class="card card--back" aria-label="Business card back">
    <svg class="card__pattern" viewBox="0 0 600 343" role="img" aria-label="Smoky grey tribal stripe ornament across the centre and right side">
      <defs>
        <linearGradient id="smokeGrey" x1="0" y1="0" x2="1" y2="1">
          <stop offset="0" stop-color="#6a6a6a" stop-opacity="0.55"/>
          <stop offset="1" stop-color="#3c3c3c" stop-opacity="0.35"/>
        </linearGradient>
      </defs>
      <path d="M200 0 C300 50 270 150 330 230 C370 290 460 320 540 343 L600 343 L600 0 Z" fill="url(#smokeGrey)"/>
    </svg>
    <ul class="card__contact">
      <li><span class="label">Phone:</span>5550193827</li>
      <li><span class="label">Email:</span>lenorapaske@fernpost.net</li>
    </ul>
    <div class="card__name">Ames K Halcott</div>
    <div class="card__role">Photographer</div>
  </section>

</main>
</body>
</html>
```